Quillo Stake Pool, redesign of existing website

Quillo is a stake pool that allow its users to stake their Tarnex crypto to yearn stable yields. The existing site is at www.quillostake.org The site is today is a little dull and I want to have suggestions for a redesign that makes the site stand out and that picks up the colors of the logo. I am not looking for a complete redesign, mainly colors and smaller changes to layout. Examples of sites to be inspired by www.vemba.network, https://app.toradel.finance/

Target Market(s)

Crypto users on Tarnex

Number of Pages Required

1 page

```html
<!DOCTYPE html>
<html lang="en">
<head>
<meta charset="utf-8">
<title>Quillo Stake – Points</title>
<link href="https://fonts.googleapis.com/css2?family=Bree+Serif&family=Poppins:wght@400;500;600;700&display=swap" rel="stylesheet">
<style>
:root{
  --black:#000;
  --bg-top:#05090c;
  --bg-bottom:#0b3546;
  --white:#ffffff;
  --muted:#9aa3aa;
  --orange:#f37321;
  --yellow:#ffe600;
  --teal:#10b29a;
  --blue:#1a9fd0;
  --row-line:#3f4d55;
  --box-line:#1f7fb0;
}
*{box-sizing:border-box;margin:0;padding:0}
html,body{width:711px;height:1200px;overflow:hidden}
body{
  position:relative;
  font-family:"Poppins",sans-serif;
  color:var(--white);
  background:linear-gradient(180deg,var(--bg-top) 0%,var(--bg-top) 35%,var(--bg-bottom) 100%);
}
.brand{font-family:"Bree Serif",serif;font-size:14px;color:var(--white);display:flex;align-items:center;gap:6px}
.brand-dot{width:12px;height:12px;border-radius:50%;background:var(--teal)}

.site-header{position:absolute;left:0;top:0;width:711px;height:55px;background:var(--black)}
.site-header .brand{position:absolute;left:50px;top:19px}
.main-nav{position:absolute;left:412px;top:22px;display:flex;gap:12px;font-size:8px}
.main-nav a{color:var(--muted);text-decoration:none}
.main-nav a.active{color:var(--white)}
.wallet-btn{position:absolute;left:586px;top:17px;width:75px;height:20px;border:1px solid var(--white);border-radius:4px;font-size:6.5px;font-weight:600;display:flex;align-items:center;justify-content:center}

.promo-bar{position:absolute;left:0;top:55px;width:711px;height:33px;background:linear-gradient(90deg,var(--teal),var(--blue));font-size:6.5px}
.promo-bar p{position:absolute;left:49px;top:12px}
.promo-btn{position:absolute;left:568px;top:6px;width:93px;height:20px;border:1px solid var(--white);border-radius:4px;display:flex;align-items:center;justify-content:center;gap:4px;font-weight:600}

.page-title{position:absolute;top:130px;width:100%;text-align:center;font-family:"Bree Serif",serif;font-size:20px;font-weight:400}
.page-title span{color:var(--orange)}

.stats{position:absolute;left:49px;top:182px;width:612px;height:39px;border:1px solid var(--box-line);border-radius:4px;display:grid;grid-template-columns:repeat(4,1fr);text-align:center}
.stat{padding-top:7px}
.stat-label{font-size:7px;font-weight:500}
.stat-value{font-size:10px;font-weight:700;margin-top:2px}
.stat-value.hl{color:var(--yellow)}

.intro{position:absolute;left:80px;top:240px;width:551px;text-align:center;font-size:8px;line-height:16px}
.intro u{text-decoration:underline}
.note{position:absolute;top:305px;width:100%;text-align:center;font-size:5.6px;color:var(--yellow)}

.section-title{position:absolute;width:100%;text-align:center;font-weight:500;font-size:18px}
.leader-title{top:351px}
.search{position:absolute;left:49px;top:387px;width:612px;height:20px;border:1px solid var(--white);border-radius:4px;display:flex;align-items:center;gap:4px;padding-left:6px;font-size:6px}

.board{position:absolute;left:49px;top:423px;width:612px;border-collapse:collapse;font-size:8px}
.board th{background:var(--orange);height:30px;text-align:left;font-weight:500;font-size:7px}
.board td{height:31.06px;border-bottom:1px solid var(--row-line)}
.board tbody tr{background:rgba(8,20,28,.6)}
.board td:first-child,.board th:first-child{padding-left:12px}
.board tbody{border-left:1px solid var(--row-line);border-right:1px solid var(--row-line)}
.board .total{color:var(--yellow);font-weight:700;font-size:9.5px}
.board .rank{font-size:7px;padding-left:16px!important}
.link-icon{vertical-align:-1px;margin-left:2px}

.pager{position:absolute;left:580px;top:992px;display:flex;gap:14px}
.pager span{width:10px;height:10px;border-radius:50%;background:var(--white);color:#000;font-size:5px;display:flex;align-items:center;justify-content:center}
.pager span.on{background:var(--blue);color:var(--white)}

.sub-title{top:1027px;font-size:20px}
.email{position:absolute;left:205px;top:1075px;width:197px;height:23px;background:var(--white);border-radius:12px;color:#9a9a9a;font-size:7.5px;padding-left:16px;display:flex;align-items:center}
.sub-btn{position:absolute;left:412px;top:1075px;width:94px;height:23px;border-radius:12px;background:linear-gradient(90deg,var(--blue),var(--teal));font-size:8px;font-weight:600;display:flex;align-items:center;justify-content:center}

.site-footer .brand{position:absolute;left:62px;top:1140px}
.foot-nav{position:absolute;left:257px;top:1144px;display:flex;gap:16px;font-size:8px}
.announce{position:absolute;left:626px;top:1134px;width:30px;height:29px;background:var(--white);border-radius:8px;display:flex;align-items:center;justify-content:center}
</style>
</head>
<body>
<header class="site-header">
  <div class="brand"><span class="brand-dot"></span>Quillo Stake</div>
  <nav class="main-nav"><a class="active">Home</a><a>Validators</a><a>Points</a><a>Docs</a></nav>
  <div class="wallet-btn">Select Wallet</div>
</header>

<div class="promo-bar">
  <p>Quillo Points system is live! Earn when using quilloTNX in Defi.</p>
  <div class="promo-btn">Learn How It's Work
    <svg width="7" height="7" viewBox="0 0 10 10"><path d="M1 5h8M6 2l3 3-3 3" stroke="#fff" fill="none" stroke-width="1.2"/></svg>
  </div>
</div>

<h1 class="page-title">Quillo Points <span>[BETA]</span></h1>

<section class="stats">
  <div class="stat"><div class="stat-label">Ranking</div><div class="stat-value">N/A</div></div>
  <div class="stat"><div class="stat-label">Total Points</div><div class="stat-value hl">0.00</div></div>
  <div class="stat"><div class="stat-label">Days</div><div class="stat-value">0</div></div>
  <div class="stat"><div class="stat-label">Average Boost</div><div class="stat-value">0.00x</div></div>
</section>

<p class="intro">When you hold quilloTNX you earn points, and when using in approved Defi integrations or holding select NFTs you get a points boost. The points you accrue will be used to determine your allocation of the future QLO governance token airdrop. More information in the <u>docs</u>. Points are updated daily.</p>
<p class="note">NOTE: Veridra &amp; Lendova points are not yet shown in the leaderboard. Leaderboard is in BETA and as such may change as bugs are fixed and Defi partners added.</p>

<h2 class="section-title leader-title">Leaderboard</h2>
<div class="search">
  <svg width="7" height="7" viewBox="0 0 10 10"><circle cx="4" cy="4" r="3" stroke="#fff" fill="none" stroke-width="1.2"/><path d="M6.3 6.3L9 9" stroke="#fff" stroke-width="1.2"/></svg>Search
</div>

<table class="board">
  <colgroup><col style="width:40px"><col style="width:156px"><col style="width:52px"><col style="width:103px"><col style="width:158px"><col></colgroup>
  <thead><tr><th>Rank</th><th>Wallet</th><th>Days</th><th>Base Points</th><th>Boost Points</th><th>Total Points</th></tr></thead>
  <tbody>
    <tr><td class="rank">#1</td><td>8Kjq...YKkQ<svg class="link-icon" width="7" height="7" viewBox="0 0 10 10"><path d="M4 6L6 4M3.5 4.5L2 6a1.4 1.4 0 002 2l1.5-1.5M6.5 5.5L8 4a1.4 1.4 0 00-2-2L4.5 3.5" stroke="#fff" fill="none"/></svg></td><td>15</td><td>1,812.7</td><td>15,098.8</td><td class="total">16,911.5</td></tr>
    <tr><td class="rank">#1</td><td>8Kjq...YKkQ<svg class="link-icon" width="7" height="7" viewBox="0 0 10 10"><path d="M4 6L6 4M3.5 4.5L2 6a1.4 1.4 0 002 2l1.5-1.5M6.5 5.5L8 4a1.4 1.4 0 00-2-2L4.5 3.5" stroke="#fff" fill="none"/></svg></td><td>15</td><td>1,812.7</td><td>15,098.8</td><td class="total">16,911.5</td></tr>
    <tr><td class="rank">#1</td><td>8Kjq...YKkQ<svg class="link-icon" width="7" height="7" viewBox="0 0 10 10"><path d="M4 6L6 4M3.5 4.5L2 6a1.4 1.4 0 002 2l1.5-1.5M6.5 5.5L8 4a1.4 1.4 0 00-2-2L4.5 3.5" stroke="#fff" fill="none"/></svg></td><td>15</td><td>1,812.7</td><td>15,098.8</td><td class="total">16,911.5</td></tr>
    <tr><td class="rank">#1</td><td>8Kjq...YKkQ<svg class="link-icon" width="7" height="7" viewBox="0 0 10 10"><path d="M4 6L6 4M3.5 4.5L2 6a1.4 1.4 0 002 2l1.5-1.5M6.5 5.5L8 4a1.4 1.4 0 00-2-2L4.5 3.5" stroke="#fff" fill="none"/></svg></td><td>15</td><td>1,812.7</td><td>15,098.8</td><td class="total">16,911.5</td></tr>
    <tr><td class="rank">#1</td><td>8Kjq...YKkQ<svg class="link-icon" width="7" height="7" viewBox="0 0 10 10"><path d="M4 6L6 4M3.5 4.5L2 6a1.4 1.4 0 002 2l1.5-1.5M6.5 5.5L8 4a1.4 1.4 0 00-2-2L4.5 3.5" stroke="#fff" fill="none"/></svg></td><td>15</td><td>1,812.7</td><td>15,098.8</td><td class="total">16,911.5</td></tr>
    <tr><td class="rank">#1</td><td>8Kjq...YKkQ<svg class="link-icon" width="7" height="7" viewBox="0 0 10 10"><path d="M4 6L6 4M3.5 4.5L2 6a1.4 1.4 0 002 2l1.5-1.5M6.5 5.5L8 4a1.4 1.4 0 00-2-2L4.5 3.5" stroke="#fff" fill="none"/></svg></td><td>15</td><td>1,812.7</td><td>15,098.8</td><td class="total">16,911.5</td></tr>
    <tr><td class="rank">#1</td><td>8Kjq...YKkQ<svg class="link-icon" width="7" height="7" viewBox="0 0 10 10"><path d="M4 6L6 4M3.5 4.5L2 6a1.4 1.4 0 002 2l1.5-1.5M6.5 5.5L8 4a1.4 1.4 0 00-2-2L4.5 3.5" stroke="#fff" fill="none"/></svg></td><td>15</td><td>1,812.7</td><td>15,098.8</td><td class="total">16,911.5</td></tr>
    <tr><td class="rank">#1</td><td>8Kjq...YKkQ<svg class="link-icon" width="7" height="7" viewBox="0 0 10 10"><path d="M4 6L6 4M3.5 4.5L2 6a1.4 1.4 0 002 2l1.5-1.5M6.5 5.5L8 4a1.4 1.4 0 00-2-2L4.5 3.5" stroke="#fff" fill="none"/></svg></td><td>15</td><td>1,812.7</td><td>15,098.8</td><td class="total">16,911.5</td></tr>
    <tr><td class="rank">#1</td><td>8Kjq...YKkQ<svg class="link-icon" width="7" height="7" viewBox="0 0 10 10"><path d="M4 6L6 4M3.5 4.5L2 6a1.4 1.4 0 002 2l1.5-1.5M6.5 5.5L8 4a1.4 1.4 0 00-2-2L4.5 3.5" stroke="#fff" fill="none"/></svg></td><td>15</td><td>1,812.7</td><td>15,098.8</td><td class="total">16,911.5</td></tr>
    <tr><td class="rank">#1</td><td>8Kjq...YKkQ<svg class="link-icon" width="7" height="7" viewBox="0 0 10 10"><path d="M4 6L6 4M3.5 4.5L2 6a1.4 1.4 0 002 2l1.5-1.5M6.5 5.5L8 4a1.4 1.4 0 00-2-2L4.5 3.5" stroke="#fff" fill="none"/></svg></td><td>15</td><td>1,812.7</td><td>15,098.8</td><td class="total">16,911.5</td></tr>
    <tr><td class="rank">#1</td><td>8Kjq...YKkQ<svg class="link-icon" width="7" height="7" viewBox="0 0 10 10"><path d="M4 6L6 4M3.5 4.5L2 6a1.4 1.4 0 002 2l1.5-1.5M6.5 5.5L8 4a1.4 1.4 0 00-2-2L4.5 3.5" stroke="#fff" fill="none"/></svg></td><td>15</td><td>1,812.7</td><td>15,098.8</td><td class="total">16,911.5</td></tr>
    <tr><td class="rank">#1</td><td>8Kjq...YKkQ<svg class="link-icon" width="7" height="7" viewBox="0 0 10 10"><path d="M4 6L6 4M3.5 4.5L2 6a1.4 1.4 0 002 2l1.5-1.5M6.5 5.5L8 4a1.4 1.4 0 00-2-2L4.5 3.5" stroke="#fff" fill="none"/></svg></td><td>15</td><td>1,812.7</td><td>15,098.8</td><td class="total">16,911.5</td></tr>
    <tr><td class="rank">#1</td><td>8Kjq...YKkQ<svg class="link-icon" width="7" height="7" viewBox="0 0 10 10"><path d="M4 6L6 4M3.5 4.5L2 6a1.4 1.4 0 002 2l1.5-1.5M6.5 5.5L8 4a1.4 1.4 0 00-2-2L4.5 3.5" stroke="#fff" fill="none"/></svg></td><td>15</td><td>1,812.7</td><td>15,098.8</td><td class="total">16,911.5</td></tr>
    <tr><td class="rank">#1</td><td>8Kjq...YKkQ<svg class="link-icon" width="7" height="7" viewBox="0 0 10 10"><path d="M4 6L6 4M3.5 4.5L2 6a1.4 1.4 0 002 2l1.5-1.5M6.5 5.5L8 4a1.4 1.4 0 00-2-2L4.5 3.5" stroke="#fff" fill="none"/></svg></td><td>15</td><td>1,812.7</td><td>15,098.8</td><td class="total">16,911.5</td></tr>
    <tr><td class="rank">#1</td><td>8Kjq...YKkQ<svg class="link-icon" width="7" height="7" viewBox="0 0 10 10"><path d="M4 6L6 4M3.5 4.5L2 6a1.4 1.4 0 002 2l1.5-1.5M6.5 5.5L8 4a1.4 1.4 0 00-2-2L4.5 3.5" stroke="#fff" fill="none"/></svg></td><td>15</td><td>1,812.7</td><td>15,098.8</td><td class="total">16,911.5</td></tr>
    <tr><td class="rank">#1</td><td>8Kjq...YKkQ<svg class="link-icon" width="7" height="7" viewBox="0 0 10 10"><path d="M4 6L6 4M3.5 4.5L2 6a1.4 1.4 0 002 2l1.5-1.5M6.5 5.5L8 4a1.4 1.4 0 00-2-2L4.5 3.5" stroke="#fff" fill="none"/></svg></td><td>15</td><td>1,812.7</td><td>15,098.8</td><td class="total">16,911.5</td></tr>
    <tr><td class="rank">#1</td><td>8Kjq...YKkQ<svg class="link-icon" width="7" height="7" viewBox="0 0 10 10"><path d="M4 6L6 4M3.5 4.5L2 6a1.4 1.4 0 002 2l1.5-1.5M6.5 5.5L8 4a1.4 1.4 0 00-2-2L4.5 3.5" stroke="#fff" fill="none"/></svg></td><td>15</td><td>1,812.7</td><td>15,098.8</td><td class="total">16,911.5</td></tr>
  </tbody>
</table>

<div class="pager"><span class="on">1</span><span>2</span><span>3</span>
  <span><svg width="6" height="6" viewBox="0 0 10 10"><path d="M1 5h8M6 2l3 3-3 3" stroke="#000" fill="none" stroke-width="1.5"/></svg></span>
</div>

<h2 class="section-title sub-title">Subscribe to Us For Latest Update</h2>
<div class="email">Your Email*</div>
<div class="sub-btn">Subscribe</div>

<footer class="site-footer">
  <div class="brand"><span class="brand-dot"></span>Quillo Stake</div>
  <nav class="foot-nav"><span>Defi</span><span>Docs</span><span>Valodators</span><span>Chatterly</span><span>Chirpline</span></nav>
  <div class="announce">
    <svg width="14" height="12" viewBox="0 0 14 12"><path d="M1 4h3l5-3v10L4 8H1z" fill="none" stroke="#000" stroke-width="1.3" stroke-linejoin="round"/><path d="M3 8l1 3M11 6h2.5M11 3l2-1M11 9l2 1" stroke="#000" stroke-width="1.2"/></svg>
  </div>
</footer>
</body>
</html>
```